New Plumbing Company

We are looking for a smart and creative business card design for our new plumbing company. We are looking for creativity and originality in our business cards.

Industry/Entity Type

Plumbing

Contact Information for Business Card

Crestline Plumbing
Peter Halvane
Managing Director
Telephone Number : 0481529604
Email : service@crestlineplumbing.com.au
Website : www.crestlineplumbing.com.au
Lic. 508264K

Colors
0692cd
33a6d7
000000

Requirements
Must have
• I want the business card to be designed on a black background using the blue tones i have selected as seen in the company logo.

```html
<!DOCTYPE html>
<html lang="en">
<head>
<meta charset="utf-8">
<title>Crestline Plumbing – Business Card</title>
<link href="https://fonts.googleapis.com/css2?family=Open+Sans:wght@400;600;700&display=swap" rel="stylesheet">
<style>
  :root {
    --backdrop: #e9e7e4;
    --card: #262627;
    --blue: #1b7fc4;
    --white: #ffffff;
    --text: #f2f2f2;
  }
  * { margin: 0; padding: 0; box-sizing: border-box; }
  html, body {
    width: 1200px; height: 1000px; overflow: hidden;
    background: var(--backdrop);
    font-family: "Open Sans", sans-serif;
  }
  .canvas { position: relative; width: 1200px; height: 1000px; }
  .card {
    position: absolute; left: 265px; width: 666px; height: 397px;
    background: var(--card); border-radius: 24px;
    box-shadow: 0 6px 14px rgba(0,0,0,0.25);
    color: var(--text);
  }
  .card--front { top: 73px; }
  .card--back { top: 532px; }

  .brand { position: absolute; display: flex; align-items: center; gap: 16px; }
  .brand__mark { border-radius: 50%; border: 4px solid var(--blue); flex: none; }
  .brand__name { color: var(--white); font-weight: 400; white-space: nowrap; letter-spacing: 0.5px; }

  .card--front .brand { left: 33px; top: 44px; }
  .card--front .brand__mark { width: 78px; height: 78px; }
  .card--front .brand__name { font-size: 30px; }

  .person { position: absolute; right: 33px; top: 195px; text-align: right; }
  .person__name { color: var(--blue); font-weight: 700; font-size: 22px; line-height: 28px; }
  .person__role { font-size: 17px; line-height: 26px; }

  .licence { position: absolute; left: 33px; top: 254px; font-size: 16px; }

  .contacts { position: absolute; left: 33px; top: 293px; list-style: none; }
  .contacts li { display: flex; align-items: center; gap: 11px; font-size: 16.5px; line-height: 25.5px; }
  .contacts svg { width: 15px; height: 15px; flex: none; }

  .card--back .brand__mark--large {
    position: absolute; left: 38px; top: 95px;
    width: 262px; height: 262px; border: 9px solid var(--blue); border-radius: 50%;
  }
  .card--back .brand { right: 33px; top: 240px; }
  .card--back .brand__name {
    font-size: 44px; line-height: 50px; text-align: right; white-space: normal;
  }
  .card--back .brand__name span { display: block; }
</style>
</head>
<body>
<main class="canvas">
  <section class="card card--front" aria-label="Business card front">
    <div class="brand">
      <span class="brand__mark"></span>
      <span class="brand__name">Crestline Plumbing</span>
    </div>
    <div class="person">
      <p class="person__name">PETER HALVANE</p>
      <p class="person__role">Managing Director</p>
    </div>
    <p class="licence">Lic. 508264K</p>
    <ul class="contacts">
      <li>
        <svg viewBox="0 0 16 16" aria-hidden="true"><path fill="#1b7fc4" d="M2 6c0-2 2-3 6-3s6 1 6 3l-3 1-1-2H6L5 7zM4 8h8l1 5H3z"/></svg>
        0481529604
      </li>
      <li>
        <svg viewBox="0 0 16 16" aria-hidden="true"><rect x="1" y="3" width="14" height="10" fill="#1b7fc4"/><path d="M1 3l7 6 7-6" fill="none" stroke="#262627" stroke-width="1.3"/></svg>
        service@crestlineplumbing.com.au
      </li>
      <li>
        <svg viewBox="0 0 16 16" aria-hidden="true"><circle cx="8" cy="8" r="6" fill="none" stroke="#1b7fc4" stroke-width="1.6"/><path d="M2 8h12M8 2c3 3 3 9 0 12M8 2c-3 3-3 9 0 12" fill="none" stroke="#1b7fc4" stroke-width="1.2"/></svg>
        www.crestlineplumbing.com.au
      </li>
    </ul>
  </section>

  <section class="card card--back" aria-label="Business card back">
    <span class="brand__mark--large" aria-hidden="true"></span>
    <div class="brand">
      <p class="brand__name"><span>Crestline</span><span>Plumbing</span></p>
    </div>
  </section>
</main>
</body>
</html>
```